Criação de Logo e Papelaria (6 itens) para PARCERIAS COM OUTRAS EMPRES. P/ LOTEAMENTOS
" VELNOR.EMPREEND. E GESTAO DE PARCERIAS LTDA. O objetivo da empresa é fazer parcerias, a tônica da ideia é a gestao das parceria contratadas . O diferencial que temos é a qualidade como sao executados os projetos e sua implantaçao. Nao é méra publicidade, a escolha e aplicaçao dos materiais é rigorosa. As ruas sao mais largas do que o exigido por lei, o paisagismo é planejado para mostrar exatamente a diferença do que fazemos. Por isso a marca deverá mostrar modernidade e qualidade. "

```html
<!DOCTYPE html>
<html lang="pt-BR">
<head>
<meta charset="UTF-8">
<title>VELNOR – Envelope</title>
<link rel="stylesheet" href="https://fonts.googleapis.com/css2?family=Archivo:wght@400;800&display=swap">
<style>
  :root {
    --brand-green: #0d6b32;
    --paper: #ffffff;
    --stage: #ffffff;
    --pattern-light: #f3f3f3;
    --pattern-mid: #cfcfcf;
    --pattern-dark: #a4a4a4;
  }
  * { margin: 0; padding: 0; box-sizing: border-box; }
  html, body {
    width: 1200px;
    height: 1200px;
    overflow: hidden;
    background: var(--stage);
  }
  .canvas {
    position: relative;
    width: 1200px;
    height: 1200px;
  }
  .envelope {
    position: absolute;
    left: 100px;
    top: 240px;
    width: 1000px;
    height: 730px;
    background: var(--paper);
    border: 1px solid #e2e2e2;
    overflow: hidden;
  }
  .envelope__edge {
    position: absolute;
    left: 0;
    top: 0;
    width: 70px;
    height: 100%;
    background: var(--brand-green);
  }
  .envelope__pattern {
    position: absolute;
    inset: 0;
    width: 100%;
    height: 100%;
  }
  .brand {
    position: absolute;
    top: 34px;
    right: 40px;
    display: flex;
    flex-direction: column;
    align-items: stretch;
    gap: 6px;
  }
  .brand__lockup {
    display: flex;
    align-items: center;
    gap: 10px;
  }
  .brand__square {
    width: 44px;
    height: 44px;
    background: var(--brand-green);
  }
  .brand__name {
    font-family: "Archivo", Arial, sans-serif;
    font-weight: 800;
    font-size: 54px;
    line-height: 1;
    letter-spacing: 1px;
    color: var(--brand-green);
  }
  .brand__tagline {
    font-family: "Archivo", Arial, sans-serif;
    font-weight: 400;
    font-size: 12px;
    line-height: 1;
    letter-spacing: 0.4px;
    color: var(--brand-green);
    white-space: nowrap;
  }
</style>
</head>
<body>
  <main class="canvas">
    <section class="envelope">
      <svg class="envelope__pattern" viewBox="0 0 1000 730" role="img"
           aria-label="Padrão decorativo em tons de cinza metálico ocupando a diagonal inferior direita do envelope">
        <defs>
          <linearGradient id="pattern-fade" x1="0" y1="1" x2="1" y2="0">
            <stop offset="0" stop-color="var(--pattern-mid)"/>
            <stop offset="0.55" stop-color="var(--pattern-light)"/>
            <stop offset="1" stop-color="var(--pattern-dark)" stop-opacity="0.6"/>
          </linearGradient>
        </defs>
        <polygon points="190,730 190,560 520,330 800,190 1000,130 1000,730"
                 fill="url(#pattern-fade)" opacity="0.7"/>
      </svg>
      <div class="envelope__edge"></div>
      <div class="brand">
        <div class="brand__lockup">
          <span class="brand__square"></span>
          <span class="brand__name">VELNOR</span>
        </div>
        <span class="brand__tagline">URBANISMO E PROJETOS INTEGRADOS LTDA.</span>
      </div>
    </section>
  </main>
</body>
</html>
```